RLW CONSTRUCTION CO POSTCARD DESIGN

I was thinking of making a postcard for mailings by printmoor and or by me dropping off at homes . I guess it would be used as a mailing post card and or flyer . I have had sketch harbor design my buisnes cards . The buisness card design is a different version from my signage on trucks because of space . I have a logo design . thyat i can upload . I like silver for back ground and black for logo and letters with glossy finish . I would like to have the RLW with a back drop to give it depth , it would be the same color as windows .

The file i submitted ha a design with red letters , this design is more detailed than the other and should be used . The colors should be black on a silver card glossy . The windows and maybe give the letters depth with a backdrop outline . I want to let home owners know that they can always call for consultation and and repairs or maintenance for their home .

Target Market(s)

home owners

Industry/Entity Type

Construction

Other font styles liked:
• The same font as used in the picture of the sign i uploaded

Requirements
Must have
• HOME IMPROVEMENTS , MAINTENANCE AND REPAIRS , CARPENTRY , TILE PAINTING ECT

```html
<!DOCTYPE html>
<html lang="en">
<head>
<meta charset="utf-8">
<title>RLW Construction Co. Postcard</title>
<link href="https://fonts.googleapis.com/css2?family=Roboto+Condensed:wght@400&family=Tinos&family=Parisienne&display=swap" rel="stylesheet">
<style>
  :root {
    --stage: #5b3019;
    --card-back: #f4f4f4;
    --ink: #111111;
    --muted: #444444;
    --accent-red: #e0201c;
    --sky-top: #5f94cf;
    --sky-mid: #cfe0f0;
    --grass: #7fbf3a;
    --stamp-line: #cfcfcf;
  }
  html, body {
    margin: 0;
    width: 1200px;
    height: 1000px;
    overflow: hidden;
    background: var(--stage);
  }
  .card {
    position: absolute;
    box-sizing: border-box;
    overflow: hidden;
  }
  /* Back of postcard */
  .card-back {
    left: 85px; top: 88px; width: 680px; height: 524px;
    background: linear-gradient(135deg, #ffffff 0%, var(--card-back) 50%, #e6e6e6 100%);
  }
  .brand-name {
    position: absolute;
    font-family: "Roboto Condensed", sans-serif;
    font-weight: 400;
    color: var(--ink);
    white-space: nowrap;
  }
  .card-back .brand-name {
    left: 42px; top: 104px; font-size: 22px; line-height: 1; letter-spacing: 0.5px;
  }
  .brand-square {
    position: absolute;
    background: var(--ink);
  }
  .card-back .brand-square { left: 42px; top: 70px; width: 24px; height: 24px; }
  .reg-number {
    position: absolute; left: 78px; top: 134px;
    font-family: "Roboto Condensed", sans-serif; font-size: 14px; color: var(--muted);
  }
  .key-photo {
    position: absolute; left: 300px; top: 22px; width: 215px; height: 145px;
    background: radial-gradient(ellipse at center, #bdbdbd 0%, #e2e2e2 55%, rgba(240,240,240,0) 75%);
  }
  .stamp-box {
    position: absolute; left: 532px; top: 34px; width: 110px; height: 112px;
    border: 1.5px solid var(--stamp-line); border-radius: 3px; background: #f7f7f7;
  }
  .intro-text {
    position: absolute; left: 31px; top: 180px; width: 292px; margin: 0;
    font-family: "Tinos", serif; font-size: 14.4px; line-height: 18px; color: var(--ink);
  }
  .mission-statement {
    position: absolute; left: 31px; top: 313px; width: 280px; margin: 0;
    font-family: "Tinos", serif; font-size: 22px; line-height: 28px; color: var(--accent-red);
  }
  /* Front of postcard */
  .card-front {
    left: 478px; top: 378px; width: 705px; height: 544px;
  }
  .scene-photo {
    position: absolute; inset: 0;
    background: linear-gradient(180deg, var(--sky-top) 0%, #9bbfe3 35%, var(--sky-mid) 70%, var(--grass) 88%, #5fa52a 100%);
  }
  .card-front .brand-square { left: 40px; top: 52px; width: 22px; height: 22px; }
  .card-front .brand-name {
    left: 40px; top: 88px; font-size: 64px; line-height: 1;
  }
  .card-front .brand-subline {
    left: 42px; top: 166px; font-size: 16px; letter-spacing: 1px;
  }
  .tagline {
    position: absolute; left: 292px; top: 100px; margin: 0;
    font-family: "Parisienne", cursive; font-size: 30px; color: var(--ink);
    transform: rotate(-6deg); transform-origin: left bottom;
  }
  .service-list {
    position: absolute; left: 36px; top: 204px; margin: 0; padding: 0; list-style: none;
    font-family: "Roboto Condensed", sans-serif; font-size: 25px; line-height: 33.5px;
    color: var(--ink); text-transform: uppercase;
    transform: scaleX(0.82); transform-origin: left top;
  }
  .contact {
    position: absolute; display: flex; align-items: flex-start; gap: 8px;
    font-family: "Roboto Condensed", sans-serif; font-size: 16px; line-height: 25px; color: var(--ink);
    white-space: nowrap;
  }
  .contact-badge {
    flex: none; width: 20px; height: 20px; margin-top: 2px; border-radius: 50%;
    background: var(--ink); color: #fff; font-size: 12px; line-height: 20px; text-align: center;
  }
  .contact-address { left: 36px; top: 392px; }
  .contact-phone { left: 36px; top: 476px; }
  .contact-email { left: 180px; top: 476px; }
  .contact-web { left: 362px; top: 476px; }
</style>
</head>
<body>
  <section class="card card-back">
    <span class="brand-square"></span>
    <span class="brand-name">RLW CONSTRUCTION CO.</span>
    <span class="reg-number">Home improvement Reg# 158734</span>
    <div class="key-photo" role="img" aria-label="Silver house key with a house-shaped keychain"></div>
    <div class="stamp-box"></div>
    <p class="intro-text">The success of a new construction project depends on the talent and dedication of the tradespeople whose job it is to bring the project to life. R L W Construction Co. has a clear mission that's been driving its success - and the success of its clients - for years. Our goals can be summed up in one simple statement:</p>
    <p class="mission-statement">Flexibility, Innovation &amp; Results - for a Lasting Partnership</p>
  </section>

  <section class="card card-front">
    <div class="scene-photo" role="img" aria-label="Blue sky with clouds over green grass, a hand holding a white paper house cutout"></div>
    <span class="brand-square"></span>
    <span class="brand-name">RLW</span>
    <span class="brand-name brand-subline">CONSTRUCTION CO.</span>
    <p class="tagline">Building Your Success</p>
    <ul class="service-list">
      <li>Construction,</li>
      <li>Home Improvements ,</li>
      <li>Maintenance and Repairs ,</li>
      <li>Carpentry ,</li>
      <li>Tile Painting ect</li>
    </ul>
    <div class="contact contact-address"><span class="contact-badge">A</span><span>R L W Construction Co.<br>27 Linden Row Easton,<br>MA 02490</span></div>
    <div class="contact contact-phone"><span class="contact-badge">P</span><span>555-204-3187</span></div>
    <div class="contact contact-email"><span class="contact-badge">E</span><span>rlwr48@mailhaven.net</span></div>
    <div class="contact contact-web"><span class="contact-badge">W</span><span>www.rlwconstructionco.com</span></div>
  </section>
</body>
</html>
```